Guarenteed! - Homepage Website Design - Coding not required- Winner to complete further pages

Hi all,

We're looking at redesigning our current website with a few adjustments to other pages but the main adjustments will be on the homepage which is what this design request is for. Please note : any of these ideas can be changed if you have something particularly different / special in mind etc.

P.S Coding is not required, just a design.

- Our website -

Our website is simply a price comparison website that allows customers to find companies within their area at the best price. The products available are mostly related to the vehicle trade and all refer to vinyl. This includes the likes of vehicle window tint, vehicle colour change vehicle wrap, vehicle signage as well as other cosmetic vinyl modifications. We allow the customer to search for their product within their chosen area and receive a list of companies who supply their product within that area. From here they can compare prices and view further details on the company.

- What we're looking to do -

We're looking first of all to adjust how the website homepage is displayed, this includes adding images and adjusting the colours that are explained below:

First of all, we look to spread out each of the 12 products (which can be seen on the website as it stands) and add an image to each of the products (all being spaced out as shown in our sketch)

We've been told the website looks too busy so we're thinking if we adjust the colours to more simplier neutral colours as well as the main focus of the website being on the 12 images, that would be great.

- Logo + Banner -

Logo to remain top left although banner may be removed / adjusted to make simplier.

- Colours -

Adjustments - Colours shades
We want the website to still look exciting but simplify the colours. Needs to be kept up to date with the colours / textures etc (bright colours to highlight keypoints)
We're still looking to use either blue or orange or maybe both to highlight these keypoints but the main website to be light colours and maybe even black on white background. The entire homepage can be adjusted colour wise if you feel it fits into your theme including menu bars, banners etc. The key is to get this right with being not too overpowering with the colours but still look interesting and up to date.

- 1 - 4 steps banner - (text may change)

This sits just under the logo and explains to the user how easy the website is to use and the steps they need to take. This may change to a 1 - 5 steps but we're looking to have this designed once the overall colours / theme of the website is sorted.

- 12 images - 4 x 3

This is the main focus of the website and will be the main focus of what the customer sees first of all. This will be where they select their product and then underneath, enter their postcode and distance they would like to search within. As explained further up, we have some of the product images available so if you can where possible add these to the design and then duplicate the images on those we currently don't have available.

- 12 Images -Titles -

These titles will be in this order from left to right and etc

- Colour Change Wrap
- Printed Vehicle Wrap
- Window Tint
- Headlight Tint
- Vehicle Signage
- Shop Signage
- Roof Vinyl Wrap
- Bonnet Vinyl Wrap
- Carbon Fibre Vinyl
- Stickerbomb Vinyl
- Clear Protective Vinyl
- Wheel Refurb

Text to be quite large, centered and with the o to the left of the title. Short titles like 'Window Tint' should fit on one line in the middle of the box where as titles such as ' Stickerbomb Vinyl Wrap' should have the 'Stickerbomb Vinyl' on the first line with the 'Wrap' on the line below. The background of this text is up to experient, might be worth just a simple colour or it might be worth using a bright blue or orange to keep in with the theme of the logo etc.

These will also have the circle tick box to the left of the title (as on the current website) where the customer clicks to select the product they have available.
We were also thinking that if when the customer ticks the circle on their selected box, the box is highlighted in some way to show this.

- Search Block -

This will appear under the 12 images and allows the customer to input their postcode and distance for the search criteria. Colours on this can of course be adjusted to keep in theme with the website.

- Under the 12 Images -

- Block underneath the 12 images and search block -

To the left will be some key bullet points about the website - maybe 4 or 5 with a green tick to the left of this. Background colour will probably be best to be a light colour, possibly grey.

Then to the right of this will appear 4 images, 2 before and 2 after when applying these products. Images to be used aren't fully decided on and we would like this stage of the design left to the end when the rest of the theme etc have been decided on.

Attached images are as follows :
- How the website looks as it stands
- The fold line on the website (obviously important)
- Our rough sketch of how we'd like the website homepage to look.
- We have 7 of the images ready that are all attached in this one file. Please duplicate the images on those that currently don't have the image available.

We will also be requesting a website developer to put this into action if our current designer falls through so please feel free to contact us if potentially interested.

The layout can change if you can think of something particular different / unique that works with this design. The main idea is to not only get the 12 products on view to the viewers but also the keypoints and before and after images.

Any questions, please ask away as we're bound to have forgotten a few things.

Thanks and good luck!

Hi all, keep the designs coming.

We haven't quite seen that extra special design we're after. As stated, we're after something fairly simple to suit the youth as well as the middle aged but we're also after something that bit special.

Colours to concentrate on are still and orange etc although feel free to use other colours if you have anything special in mind.

Please experience and we'll give you our honest feedback.

Many thanks all and good luck!

Hi all, this is a message to all the designers.

Some good designs coming in but we're still after that something special for the website design. Keep the designs coming and please feel free to experiment with the design colours, layout etc.

The basic principle of the website needs to remain regarding the 12 products, search within block and 4 steps all appearing on the homepage.

The 4 steps seems to work best when it's got text as well as some simple images next to this.

A variation with the product titles with how to display this, some designers have gone with a simple white background whereas others have gone with colours. Please experiment here and where possible, add a contract / texture to the colour. Please remember the product titles needs to be clear, centured and with the circle tick box to the left of it. 

We're after a fairly simple design although we need it to look 21st century, up to date as well as interesting. The key points straight away are the 4 steps as well as the 12 products so try to guide the viewer to these areas a little.

White background behind the 12 images seems to be a much, although a light colour could possibly work.

The keypoints underneath these 12 products are too very important as it outlines what we do etc. Tick colour can vary.

Next to these keypoints will be the 'before' and 'after' images, these images needs to be fairly small and ensure there is white background around the image itself.

Good luck all and any questions, feel free to ask away.

Thanks!

Hi,

 Thank you for your time and effort with these designs, we are very nearly there with the design but we've thought of something that may work for the homepage. A curved arrow from step 1 pointing to the products, this may or may not work but feel free to give it a go.

Many thanks,

Thank you to everyone for your time and efforts with the design. It's hugely appreciated so thank you all once again.

Wish you all the luck in the future.

```html
<!DOCTYPE html>
<html lang="en">
<head>
<meta charset="utf-8">
<title>Wrap Locator – Homepage</title>
<link rel="stylesheet" href="https://fonts.googleapis.com/css2?family=Open+Sans:wght@400;600;700;800&display=swap">
<style>
  :root {
    --navy: #2f3d66;
    --navy-dark: #243154;
    --orange: #f7941d;
    --banner-bg: #eef0f4;
    --footer-bg: #e8eaee;
    --card-bg: #f3f4f6;
    --text: #3b3f48;
    --muted: #8a8f99;
    --white: #ffffff;
    --line: #d9dce2;
  }
  * { box-sizing: border-box; margin: 0; padding: 0; }
  html, body { width: 870px; height: 1200px; overflow: hidden; background: var(--white); }
  body { font-family: "Open Sans", Arial, sans-serif; color: var(--text); font-size: 11px; }
  .page { width: 680px; margin: 0 auto; position: relative; height: 1200px; }

  /* Header */
  .site-header { height: 81px; display: flex; align-items: center; justify-content: space-between; }
  .brand { display: flex; align-items: center; gap: 8px; }
  .brand-mark { width: 26px; height: 26px; border-radius: 50%; background: var(--orange); }
  .brand-name { font-size: 22px; font-weight: 800; color: var(--navy); letter-spacing: .5px; text-transform: uppercase; }
  .site-search { display: flex; }
  .site-search input { width: 150px; height: 24px; border: 1px solid var(--line); padding: 0 8px; font: inherit; color: var(--muted); }
  .site-search button { width: 50px; height: 24px; border: 0; background: var(--orange); color: var(--white); font: 600 11px "Open Sans", Arial, sans-serif; }
  .free-phone { text-align: right; color: var(--navy); line-height: 1.1; }
  .free-phone .label { display: inline-block; background: var(--navy); color: var(--white); font-weight: 800; font-size: 11px; padding: 2px 6px; text-transform: uppercase; }
  .free-phone .number { font-size: 17px; font-weight: 800; color: var(--orange); }

  /* Steps nav */
  .steps-nav { height: 58px; background: var(--navy); display: flex; }
  .step { flex: 1; display: flex; align-items: center; justify-content: center; text-align: center; color: var(--white); font-size: 10px; font-weight: 700; text-transform: uppercase; line-height: 1.3; padding: 0 8px; border-right: 1px solid rgba(255,255,255,.15); }
  .step.is-active { background: var(--white); color: var(--navy); border-top: 3px solid var(--navy); }
  .follow { width: 110px; flex: none; padding: 0 10px; display: flex; flex-direction: column; justify-content: center; color: var(--white); font-weight: 700; font-size: 10px; text-transform: uppercase; }
  .social { display: flex; gap: 4px; margin-top: 4px; }
  .social span { width: 16px; height: 16px; background: #5c6b94; }

  /* Banner */
  .hero { height: 175px; background: var(--banner-bg); display: flex; position: relative; }
  .hero-copy { width: 360px; padding: 16px 0 0 18px; }
  .hero-title { font-size: 34px; font-weight: 700; color: var(--orange); line-height: 1.1; }
  .hero-text { margin-top: 6px; font-size: 10.5px; line-height: 1.45; color: var(--text); width: 320px; }
  .locate { margin-top: 10px; display: flex; align-items: center; gap: 8px; color: var(--navy); text-transform: uppercase; font-weight: 800; }
  .locate .small { font-size: 13px; display: block; line-height: 1; }
  .locate .big { font-size: 26px; display: block; line-height: 1; }
  .hero-image { position: absolute; right: 12px; top: 30px; width: 290px; height: 140px; border-radius: 18px 40px 8px 8px; background: linear-gradient(180deg, #ffffff 0%, #dfe2e7 100%); box-shadow: inset 0 -12px 0 #c9ccd2; }

  /* Products */
  .products { display: grid; grid-template-columns: repeat(4, 160px); gap: 10px 13px; margin-top: 12px; }
  .product { height: 198px; background: var(--white); border: 1px solid var(--line); display: flex; flex-direction: column; }
  .product-image { height: 110px; background: var(--card-bg); position: relative; display: flex; align-items: center; justify-content: center; }
  .product-image .art { width: 120px; height: 72px; border-radius: 30px 30px 10px 10px; }
  .product-info { flex: 1; padding: 8px 10px; background: var(--card-bg); border-top: 1px solid var(--line); }
  .product-title { font-size: 12px; font-weight: 700; color: var(--navy); }
  .product-text { margin-top: 4px; font-size: 9.5px; color: var(--muted); line-height: 1.4; }
  .product.is-selected { border: 2px solid var(--navy); }
  .product.is-selected .product-image::after { content: ""; position: absolute; inset: 0; background: rgba(47,61,102,.45); }
  .quick-view { position: absolute; z-index: 1; background: var(--white); color: var(--navy); font-size: 10px; font-weight: 700; padding: 4px 10px; }
  .product.is-selected .product-info { background: var(--navy); }
  .product.is-selected .product-title, .product.is-selected .product-text { color: var(--white); }

  /* Mailing list */
  .mailing { margin-top: 14px; height: 50px; background: var(--navy); display: flex; align-items: center; padding: 0 18px; gap: 10px; }
  .mailing h2 { color: var(--white); font-size: 20px; font-weight: 600; margin-right: auto; }
  .mailing input { width: 120px; height: 22px; border: 0; padding: 0 6px; font: 10px "Open Sans", Arial, sans-serif; color: var(--muted); }
  .mailing button { height: 22px; padding: 0 12px; border: 0; background: var(--orange); color: var(--white); font: 600 11px "Open Sans", Arial, sans-serif; }

  /* Footer */
  .site-footer { background: var(--footer-bg); height: 170px; display: flex; gap: 20px; padding: 14px 18px 0; }
  .footer-col h3 { font-size: 12px; font-weight: 700; color: var(--navy); margin-bottom: 6px; }
  .footer-col li { list-style: none; font-size: 9.5px; color: var(--text); line-height: 1.6; }
  .footer-col p { font-size: 9.5px; line-height: 1.5; color: var(--text); }
  .col-links { width: 170px; }
  .col-location { width: 180px; }
  .col-photo { width: 120px; }
  .photo { background: var(--white); padding: 5px; border: 1px solid var(--line); }
  .photo div { height: 90px; background: linear-gradient(180deg, #8ed36b 0%, #3f9c2f 100%); border-radius: 6px; }
  .copyright { text-align: center; font-size: 9px; color: var(--muted); padding: 8px 0; background: var(--footer-bg); }
</style>
</head>
<body>
<div class="page">
  <header class="site-header">
    <div class="brand"><span class="brand-mark"></span><span class="brand-name">Wrap Locator</span></div>
    <form class="site-search"><input type="text" value="Search..."><button type="button">Search</button></form>
    <div class="free-phone"><span class="label">Free Phone</span><div class="number">0800 555 0142</div></div>
  </header>

  <nav class="steps-nav">
    <div class="step is-active">Select Chosen<br>Product</div>
    <div class="step">Input Postcode,<br>Distance &amp; Search</div>
    <div class="step">Campare Campaigns<br>&amp; Prices</div>
    <div class="step">Contact<br>Chosen Company</div>
    <div class="follow">Follow Us<div class="social"><span></span><span></span><span></span><span></span></div></div>
  </nav>

  <section class="hero">
    <div class="hero-copy">
      <h1 class="hero-title">Vehicle Signage</h1>
      <p class="hero-text">Professional vehicle signage fitted by trusted local installers. Compare prices from approved companies in your area and choose the best quote for your van, car or fleet.</p>
      <div class="locate">
        <div><span class="small">Find a Location</span><span class="big">Click Hear</span></div>
        <svg width="26" height="32" viewBox="0 0 26 32"><path d="M13 1C6.4 1 1 6.2 1 12.6 1 21 13 31 13 31s12-10 12-18.4C25 6.2 19.6 1 13 1z" fill="none" stroke="#2f3d66" stroke-width="3"/><circle cx="13" cy="12.5" r="4" fill="#2f3d66"/></svg>
      </div>
    </div>
    <div class="hero-image" role="img" aria-label="White panel van with company signage"></div>
  </section>

  <section class="products">
    <article class="product is-selected">
      <div class="product-image"><div class="art" role="img" aria-label="Car with black vinyl wrapped roof" style="background:linear-gradient(180deg,#222 0 30%,#e9eaec 30%)"></div><span class="quick-view">Quick View</span></div>
      <div class="product-info"><h3 class="product-title">Roof Vinyl Wrap</h3><p class="product-text">Expert fitters near you, compare quotes and prices.</p></div>
    </article>
    <article class="product">
      <div class="product-image"><div class="art" role="img" aria-label="Car covered in colourful stickerbomb vinyl" style="background:linear-gradient(120deg,#e94b3c,#f7c325,#3fa9f5,#8bc34a)"></div></div>
      <div class="product-info"><h3 class="product-title">Stickerbomb Vinyl</h3><p class="product-text">Expert fitters near you, compare quotes and prices.</p></div>
    </article>
    <article class="product">
      <div class="product-image"><div class="art" role="img" aria-label="Green car with tinted windows" style="background:linear-gradient(180deg,#2c3a2c 0 35%,#4cbb3a 35%)"></div></div>
      <div class="product-info"><h3 class="product-title">Window Tint</h3><p class="product-text">Expert fitters near you, compare quotes and prices.</p></div>
    </article>
    <article class="product">
      <div class="product-image"><div class="art" role="img" aria-label="Shop front with vinyl signage" style="border-radius:2px;background:linear-gradient(180deg,#6b7078 0 25%,#d5d8dd 25%)"></div></div>
      <div class="product-info"><h3 class="product-title">Shop Signage</h3><p class="product-text">Expert fitters near you, compare quotes and prices.</p></div>
    </article>
    <article class="product">
      <div class="product-image"><div class="art" role="img" aria-label="Car with printed green wrap" style="background:linear-gradient(135deg,#9ad46a,#3f8f2e)"></div></div>
      <div class="product-info"><h3 class="product-title">Printed Vehicle Wrap</h3><p class="product-text">Expert fitters near you, compare quotes and prices.</p></div>
    </article>
    <article class="product">
      <div class="product-image"><div class="art" role="img" aria-label="Silver car with vinyl wrapped bonnet" style="background:linear-gradient(180deg,#8d9298,#c8ccd1)"></div></div>
      <div class="product-info"><h3 class="product-title">Bonnet Vinyl Wrap</h3><p class="product-text">Expert fitters near you, compare quotes and prices.</p></div>
    </article>
    <article class="product">
      <div class="product-image"><div class="art" role="img" aria-label="Car after red colour change wrap" style="background:linear-gradient(180deg,#e53935,#a61b1b)"></div></div>
      <div class="product-info"><h3 class="product-title">Colour Change Wrap</h3><p class="product-text">Expert fitters near you, compare quotes and prices.</p></div>
    </article>
    <article class="product">
      <div class="product-image"><div class="art" role="img" aria-label="White van with vehicle signage" style="background:linear-gradient(180deg,#ffffff,#cfd3d9)"></div></div>
      <div class="product-info"><h3 class="product-title">Vehicle Signage</h3><p class="product-text">Expert fitters near you, compare quotes and prices.</p></div>
    </article>
    <article class="product">
      <div class="product-image"><div class="art" role="img" aria-label="White car with carbon fibre vinyl details" style="background:linear-gradient(180deg,#f2f2f2 0 60%,#2a2a2a 60%)"></div></div>
      <div class="product-info"><h3 class="product-title">Carbon Fibre Vinyl</h3><p class="product-text">Expert fitters near you, compare quotes and prices.</p></div>
    </article>
    <article class="product">
      <div class="product-image"><div class="art" role="img" aria-label="Car headlight with tint film" style="background:linear-gradient(135deg,#cfe3f5,#3d8fd6)"></div></div>
      <div class="product-info"><h3 class="product-title">Headlight Tint</h3><p class="product-text">Expert fitters near you, compare quotes and prices.</p></div>
    </article>
    <article class="product">
      <div class="product-image"><div class="art" role="img" aria-label="Red sports car with clear protective film" style="background:linear-gradient(180deg,#d32f2f,#7f1313)"></div></div>
      <div class="product-info"><h3 class="product-title">Clear Protective Vinyl</h3><p class="product-text">Expert fitters near you, compare quotes and prices.</p></div>
    </article>
    <article class="product">
      <div class="product-image"><div class="art" role="img" aria-label="Red car with refurbished wheels" style="background:linear-gradient(180deg,#e53935 0 65%,#3a3a3a 65%)"></div></div>
      <div class="product-info"><h3 class="product-title">Wheel Refurb</h3><p class="product-text">Expert fitters near you, compare quotes and prices.</p></div>
    </article>
  </section>

  <section class="mailing">
    <h2>Join our mailing List</h2>
    <input type="text" value="Name">
    <input type="text" value="Email">
    <button type="button">Subscribe</button>
  </section>

  <footer class="site-footer">
    <div class="footer-col col-links">
      <h3>Link</h3>
      <ul>
        <li>Select Chosen Product</li>
        <li>Input Postcode, Distance &amp; Search</li>
        <li>Compare campaigns &amp; prices</li>
        <li>Contact Chosen Company</li>
        <li>Terms &amp; conditions</li>
      </ul>
    </div>
    <div class="footer-col col-location">
      <h3>Location</h3>
      <p>Visit our office during working hours, Monday to Friday.</p>
      <p style="margin-top:6px">Address: 12 Sample Road,<br>Leeds LS1 0AA</p>
      <p>Phone: 0800 555 0142</p>
      <p>Fax: 0800 555 0143</p>
      <p>Email: hello@wraplocator.example</p>
    </div>
    <div class="footer-col col-photo">
      <h3>Before</h3>
      <div class="photo"><div role="img" aria-label="Green car before vinyl is applied"></div></div>
    </div>
    <div class="footer-col col-photo">
      <h3>After</h3>
      <div class="photo"><div role="img" aria-label="Green car after vinyl is applied" style="background:linear-gradient(180deg,#a7e07f,#2f8a24)"></div></div>
    </div>
  </footer>
  <div class="copyright">Wrap Locator © 2013 • Privacy Policy</div>
</div>
</body>
</html>
```